Corwith Lodge website redesign

After 8 years of our current site, we're ready to upgrade our site design. We'd like to generally make it more modern and clean and build it on a CMS like joomla for easier future maintenance.

Our hotel is a family-owned bed and breakfast that competes against much larger hotel chains in Aspen with fancier rooms and larger pricetags. Our hotel is priced moderately and features tasteful, uniquely-design rooms.

We are looking for a website that will showcase the uniqueness of our rooms, the history of the Lodge, and the friendliness of our staff.

Here are some other hotel sites we like:

http://www.brackenfoldhouse.example/

http://www.tollerpeakhaus.example/

http://www.quarrowstay.example/

*********

Scope of Work - I'm looking for a design AND build. The website should be built out in Joomla as part of the final deliverable.
Updates

Current website: http://www.corwithlodge.example/

Explanation of what design + build means:

I am looking for not only the design of the site, but also for the homepage and one subpage to be built out as well. I do NOT need the entire site built - only for those two pages to be built and I will retrofit the remainder of the pages.

Target Market(s)

travellers evaluating hotels in Aspen, Colorado.

Industry/Entity Type

Hotel

Requirements
Must have
• Must, must, must be based on a joomla template. "Rotating" large main image as central position on homepage is a must (see example websites mentioned above).

Nice to have
• We have an existing online reservation system. It would be nice to evaluate placing a "widget" on the homepage that integrates to the online reservation page. Similar to that feature that the Bracken Fold website has at the foot of the main image on their homepage.

```html
<!DOCTYPE html>
<html lang="en">
<head>
<meta charset="utf-8">
<title>Corwith Lodge – Luxurious in Aspen</title>
<link rel="stylesheet" href="https://fonts.googleapis.com/css2?family=Questrial&family=Cutive&family=Noto+Sans:wght@400;700;800&display=swap">
<style>
  :root {
    --ink: #111111;
    --paper: #ffffff;
    --lime: #b5d12f;
    --lime-dark: #8fb01c;
    --field: #9c9c9c;
    --panel: rgba(20, 18, 16, 0.82);
    --rule: #222222;
    --muted: #333333;
  }
  * { box-sizing: border-box; margin: 0; padding: 0; }
  html, body { width: 1200px; height: 831px; overflow: hidden; background: var(--paper); }
  body { position: relative; font-family: "Questrial", sans-serif; color: var(--ink); }

  .brand { position: absolute; left: 159px; top: 20px; font-family: "Questrial", sans-serif; font-size: 31px; color: var(--ink); letter-spacing: 0.5px; }

  .contact { position: absolute; right: 170px; top: 18px; text-align: right; font-size: 14.5px; line-height: 17px; }
  .contact .label { color: var(--lime); }

  .main-nav { position: absolute; top: 77px; left: 0; width: 1200px; height: 22px; font-size: 17px; }
  .main-nav a { position: absolute; color: var(--ink); text-decoration: none; white-space: nowrap; }

  .hero { position: absolute; left: 159px; top: 104px; width: 867px; height: 406px;
    background: linear-gradient(160deg, #5c5347 0%, #7a5a3e 35%, #4a3a2c 60%, #cfcac6 78%, #efeeee 100%); }
  .hero-title { position: absolute; left: 319px; top: 196px; font-family: "Cutive", serif; color: #fff; font-size: 41px; line-height: 72px; white-space: nowrap; }

  .booking { position: absolute; left: 28px; top: 102px; width: 219px; height: 239px; border-radius: 11px; background: var(--panel); }
  .booking label { position: absolute; color: var(--lime); font-size: 13.5px; }
  .booking .field { position: absolute; height: 17px; background: var(--field); border: 1px solid #b4b4b4; }
  .booking .select svg { position: absolute; right: 5px; top: 5px; }
  .booking .submit { position: absolute; left: 20px; top: 181px; width: 180px; height: 17px; border: 0;
    background: linear-gradient(#e4f27a, var(--lime) 50%, var(--lime-dark)); font-family: "Questrial", sans-serif; font-size: 13px; color: #222; }

  .features { position: absolute; left: 159px; top: 524px; width: 867px; height: 254px; }
  .features .rule-left { position: absolute; left: 0; top: 0; height: 254px; border-left: 1px dotted var(--rule); }
  .features .rule-mid { position: absolute; left: 593px; top: 0; height: 254px; border-left: 1px dotted var(--rule); }
  .features .rule-right { position: absolute; left: 866px; top: 0; height: 254px; border-left: 1px dotted var(--rule); }

  .teaser { position: absolute; width: 240px; font-family: "Noto Sans", sans-serif; }
  .teaser .icon { position: absolute; left: 0; top: 0; }
  .teaser h3 { position: absolute; left: 36px; top: 1px; font-size: 12.5px; font-weight: 800; letter-spacing: 0.9px; white-space: nowrap; }
  .teaser p { position: absolute; left: 36px; top: 18px; width: 170px; font-size: 12.5px; line-height: 15px; color: var(--muted); }
  .teaser .more { display: inline-block; vertical-align: -2px; margin-left: 3px; }

  .rates h3 { position: absolute; left: 643px; top: 30px; font-family: "Noto Sans", sans-serif; font-size: 12.5px; font-weight: 800; letter-spacing: 0.9px; }
  .rates .marker { position: absolute; left: 630px; top: 24px; width: 4px; height: 20px; background: var(--ink); }
  .rates .photo { position: absolute; left: 631px; top: 60px; width: 199px; height: 163px;
    background: linear-gradient(135deg, #6a4a3a 0%, #8c3c34 35%, #3d2a22 65%, #b7b0a4 100%); }

  .footer-rule { position: absolute; left: 159px; top: 794px; width: 870px; height: 5px; background: var(--ink); }
  .copyright { position: absolute; left: 159px; top: 808px; font-family: "Noto Sans", sans-serif; font-weight: 700; font-size: 12px; letter-spacing: 0.6px; }
</style>
</head>
<body>
  <header>
    <div class="brand">Corwith Lodge</div>
    <div class="contact">
      <div><span class="label">email</span> info@corwithlodge.example</div>
      <div><span class="label">telefone number</span> 0077 555 0142</div>
    </div>
    <nav class="main-nav">
      <a href="#" style="left:159px">About the Lodge</a>
      <a href="#" style="left:290px">Rooms</a>
      <a href="#" style="left:375px">Amenities</a>
      <a href="#" style="left:481px">Aspen information</a>
      <a href="#" style="left:653px">Manager´s journal</a>
      <a href="#" style="left:833px">Webcams</a>
      <a href="#" style="left:947px">Contact us</a>
    </nav>
  </header>

  <section class="hero" role="img" aria-label="Photo of the lodge entrance with timber porch and stone walls in winter snow">
    <form class="booking">
      <label style="left:21px;top:31px">Arrival</label>
      <div class="field" style="left:20px;top:47px;width:180px"></div>
      <label style="left:21px;top:70px">Departur</label>
      <div class="field" style="left:20px;top:86px;width:180px"></div>
      <label style="left:23px;top:110px">Adults</label>
      <label style="left:120px;top:110px">Children</label>
      <div class="field select" style="left:22px;top:126px;width:82px">
        <svg width="10" height="6" viewBox="0 0 10 6"><path d="M1 1l4 4 4-4" fill="none" stroke="#444" stroke-width="1.3"/></svg>
      </div>
      <div class="field select" style="left:118px;top:126px;width:82px">
        <svg width="10" height="6" viewBox="0 0 10 6"><path d="M1 1l4 4 4-4" fill="none" stroke="#444" stroke-width="1.3"/></svg>
      </div>
      <button class="submit" type="button">Submit</button>
    </form>
    <h1 class="hero-title">Luxurious in Aspen<br>ski bed &amp; breakfasts</h1>
  </section>

  <main class="features">
    <div class="rule-left"></div>
    <div class="rule-mid"></div>
    <div class="rule-right"></div>

    <article class="teaser" style="left:37px;top:30px">
      <svg class="icon" width="24" height="21" viewBox="0 0 24 21"><rect width="24" height="21" rx="3" fill="#111"/><path d="M6 5l5 5.5-5 5.5M12 5l5 5.5-5 5.5" fill="none" stroke="#fff" stroke-width="1.8"/></svg>
      <h3>HISTORY OF THE LODGE</h3>
      <p>The Corwith Lodge was founded in 1948<svg class="more" width="12" height="12" viewBox="0 0 12 12"><path d="M1 1l4.5 5L1 11M6 1l4.5 5L6 11" fill="none" stroke="#b5d12f" stroke-width="2"/></svg></p>
    </article>

    <article class="teaser" style="left:321px;top:30px">
      <svg class="icon" width="24" height="21" viewBox="0 0 24 21"><rect width="24" height="21" rx="3" fill="#111"/><path d="M6 5l5 5.5-5 5.5M12 5l5 5.5-5 5.5" fill="none" stroke="#fff" stroke-width="1.8"/></svg>
      <h3>CONFERENCE FACILITY</h3>
      <p>Remember the Corwith Lodge when you're planning an event<svg class="more" width="12" height="12" viewBox="0 0 12 12"><path d="M1 1l4.5 5L1 11M6 1l4.5 5L6 11" fill="none" stroke="#b5d12f" stroke-width="2"/></svg></p>
    </article>

    <article class="teaser" style="left:37px;top:148px">
      <svg class="icon" width="24" height="21" viewBox="0 0 24 21"><rect width="24" height="21" rx="3" fill="#111"/><path d="M6 5l5 5.5-5 5.5M12 5l5 5.5-5 5.5" fill="none" stroke="#fff" stroke-width="1.8"/></svg>
      <h3>UNIQUE ROOMS</h3>
      <p>Are you looking for a unique place to stay in the heart of Aspen?<svg class="more" width="12" height="12" viewBox="0 0 12 12"><path d="M1 1l4.5 5L1 11M6 1l4.5 5L6 11" fill="none" stroke="#b5d12f" stroke-width="2"/></svg></p>
    </article>

    <article class="teaser" style="left:321px;top:148px">
      <svg class="icon" width="24" height="21" viewBox="0 0 24 21"><rect width="24" height="21" rx="3" fill="#111"/><path d="M6 5l5 5.5-5 5.5M12 5l5 5.5-5 5.5" fill="none" stroke="#fff" stroke-width="1.8"/></svg>
      <h3>HOW TO GET THERE</h3>
      <p>Driving Directions from Denver<svg class="more" width="12" height="12" viewBox="0 0 12 12"><path d="M1 1l4.5 5L1 11M6 1l4.5 5L6 11" fill="none" stroke="#b5d12f" stroke-width="2"/></svg></p>
    </article>

    <aside class="rates">
      <div class="marker"></div>
      <h3>ROOMS &amp; RATES</h3>
      <div class="photo" role="img" aria-label="Photo of the lodge reception desk with flower arrangement and lamp"></div>
    </aside>
  </main>

  <footer>
    <div class="footer-rule"></div>
    <div class="copyright">copyright: xxx xxxxxx</div>
  </footer>
</body>
</html>
```